Business Card Design

I would like a logo created for the top left corner of the card please. I would like a checkerboard in a dark navy with the edges fading out and one random bright orange square.
Updates

I have attached some further notes and a really rough sketch of what I am after.  Thank you. :)

Target Market(s)

Construction, mining, mechanical

Industry/Entity Type

Business

Contact Information for Business Card

Korvane Works Pty Ltd, Glen Hadwick, P. 0418365072, F. 0736209158, E.glen@korvaneworks.com.au, PO Box 87 YARRAWONGA Q 4581, ABN 53209874611

Font styles to use
Sans Serif

Requirements
Must have
• Really Dark Navy
Really bright Orange

```html
<!DOCTYPE html>
<html lang="en">
<head>
<meta charset="utf-8">
<title>Korvane Works Pty Ltd — Business Card</title>
<link rel="stylesheet" href="https://fonts.googleapis.com/css2?family=Roboto+Condensed:ital,wght@0,400;0,700;1,400;1,700&display=swap">
<style>
  :root {
    --navy: #022a35;
    --orange: #ff7f0a;
    --paper: #ffffff;
  }
  html, body {
    margin: 0;
    padding: 0;
    width: 1200px;
    height: 726px;
    overflow: hidden;
    background: var(--paper);
  }
  .card {
    position: relative;
    width: 1200px;
    height: 726px;
    background: var(--paper);
    color: var(--navy);
    font-family: "Roboto Condensed", "Arial Narrow", sans-serif;
  }
  .brand-mark {
    position: absolute;
    left: 40px;
    top: 124px;
    display: flex;
    align-items: center;
    gap: 14px;
  }
  .brand-mark__square {
    width: 60px;
    height: 60px;
    background: var(--orange);
  }
  .brand-mark__name {
    font-size: 30px;
    font-weight: 700;
    color: var(--navy);
    white-space: nowrap;
  }
  .company-name {
    position: absolute;
    left: 380px;
    top: 136px;
    margin: 0;
    font-size: 47px;
    font-weight: 700;
    letter-spacing: -0.3px;
    line-height: 1;
  }
  .contact {
    position: absolute;
    left: 380px;
    top: 390px;
    margin: 0;
    font-style: italic;
    font-size: 34px;
    line-height: 51px;
  }
  .contact__name {
    font-weight: 700;
  }
  .contact__line {
    display: block;
    font-weight: 400;
    white-space: nowrap;
  }
</style>
</head>
<body>
  <div class="card">
    <div class="brand-mark">
      <div class="brand-mark__square"></div>
      <span class="brand-mark__name">Korvane Works</span>
    </div>

    <h1 class="company-name">Korvane Works Pty Ltd</h1>

    <address class="contact">
      <span class="contact__line contact__name">Glen Hadwick</span>
      <span class="contact__line">P. 0418365072</span>
      <span class="contact__line">F. 0736209158</span>
      <span class="contact__line">E.glen@korvaneworks.com.au</span>
      <span class="contact__line">PO Box 87 YARRAWONGA Q 4581, ABN 53209874611</span>
    </address>
  </div>
</body>
</html>
```